Pelton|Marsh & Quillan business card contest

We need a logo for an upscale boutique diversified company involved in real estate, investments, cattle, and more. Our businesses DO NOT need to be reflected in the business card nor do we want them noted. This is our logo and colors and we love our logo and colors. Our logo looks best against a black background and we like to include the firm name in our logo usage. importantly, the names Pelton and Marsh are separated by | not / and we use an ampersand not the word and.
On the front of the card, we want to include:
company logo and name (Pelton|Marsh & Quillan)
on the back, we would definitely include:
address, email, cell #
logo and name (smaller size than front)

The variable will be location of individual name and title (mine for example is ) - whether on the front OR on the back. interested in variations from which to choose
Dr. Neil R. Whitcombe, CFA
Scientifique des Fusées Financières

we would like to use contemporary symbols for address, email address, cell # with an option for web site that we do not intend to use initially. we like two sided cards and believe this design should use four rounded corners with the standard size. we prefer thicker card stock and may look at metal.

```html
<!DOCTYPE html>
<html lang="en">
<head>
<meta charset="utf-8">
<title>Pelton|Marsh &amp; Quillan — Business Card</title>
<link href="https://fonts.googleapis.com/css2?family=Questrial&family=Montserrat:wght@600&display=swap" rel="stylesheet">
<style>
  :root {
    --backdrop: #b3b3b3;
    --card-light: #ffffff;
    --card-dark: #000000;
    --brand-orange: #dd7620;
    --brand-orange-deep: #c9621a;
    --brand-grey: #646464;
    --ink: #111111;
    --rule: #7a7a7a;
  }
  * { margin: 0; padding: 0; box-sizing: border-box; }
  html, body {
    width: 1200px; height: 848px; overflow: hidden;
    background: var(--backdrop);
  }
  .stage { position: relative; width: 1200px; height: 848px; }

  .card {
    position: absolute;
    border-radius: 24px;
    overflow: hidden;
  }
  .card--front { left: 380px; top: 38px; width: 506px; height: 330px; background: var(--card-light); }
  .card--back  { left: 378px; top: 424px; width: 511px; height: 332px; background: var(--card-dark); }

  .brand {
    position: absolute;
    display: flex; flex-direction: column; align-items: center;
    font-family: "Questrial", sans-serif;
    color: var(--brand-grey);
    white-space: nowrap;
  }
  .brand__mark { background: var(--brand-orange); }
  .card--front .brand { left: 0; width: 221px; top: 114px; }
  .card--front .brand__mark { width: 26px; height: 26px; margin-bottom: 14px; }
  .card--front .brand__name { font-size: 17px; }
  .card--back .brand { left: 0; width: 511px; top: 84px; }
  .card--back .brand__mark { width: 52px; height: 52px; margin-bottom: 34px; }
  .card--back .brand__name { font-size: 36px; }

  .divider {
    position: absolute; left: 220px; top: 60px;
    width: 1.5px; height: 211px; background: var(--rule);
  }

  .person {
    position: absolute; left: 222px; width: 274px; top: 86px;
    text-align: center;
  }
  .person__name {
    font-family: "Questrial", sans-serif;
    font-size: 19.5px; color: var(--ink); line-height: 1;
  }
  .person__title {
    margin-top: 9px;
    font-family: "Questrial", sans-serif;
    font-size: 9.2px; letter-spacing: 0.3px; color: var(--brand-orange);
  }

  .contacts { position: absolute; left: 237px; top: 169px; list-style: none; }
  .contacts__item {
    display: flex; align-items: center; height: 16px; margin-bottom: 7.6px;
    font-family: "Montserrat", sans-serif; font-weight: 600;
    font-size: 8.3px; letter-spacing: 0.6px; color: var(--ink);
  }
  .contacts__icon {
    width: 16px; height: 16px; border-radius: 50%;
    background: var(--brand-orange-deep);
    display: flex; align-items: center; justify-content: center;
    margin-right: 7px; flex: none;
  }
  .contacts__icon svg { width: 9px; height: 9px; }
</style>
</head>
<body>
<main class="stage">

  <section class="card card--front" aria-label="Card front">
    <div class="brand">
      <span class="brand__mark"></span>
      <span class="brand__name">Pelton|Marsh &amp; Quillan</span>
    </div>

    <div class="divider"></div>

    <div class="person">
      <p class="person__name">Dr. Neil R. Whitcombe, CFA</p>
      <p class="person__title">Scientifique des Fusées Financières</p>
    </div>

    <ul class="contacts">
      <li class="contacts__item">
        <span class="contacts__icon">
          <svg viewBox="0 0 10 10"><path d="M5 0.5a3 3 0 0 0-3 3c0 2.3 3 6 3 6s3-3.7 3-6a3 3 0 0 0-3-3z" fill="#fff"/><circle cx="5" cy="3.5" r="1.1" fill="#c9621a"/></svg>
        </span>
        4280 Larkspurton PKWY S FARGO,ND 58104-2217
      </li>
      <li class="contacts__item">
        <span class="contacts__icon">
          <svg viewBox="0 0 10 10"><path d="M2.2 1.2l1.4-.3 1 2-1 .8c.5 1.1 1.4 2 2.5 2.5l.8-1 2 1-.3 1.4C7.2 8.9 1.1 2.8 2.2 1.2z" fill="#fff"/></svg>
        </span>
        701 555 0148
      </li>
      <li class="contacts__item">
        <span class="contacts__icon">
          <svg viewBox="0 0 10 10" fill="none" stroke="#fff" stroke-width="0.8"><circle cx="5" cy="5" r="4"/><ellipse cx="5" cy="5" rx="1.8" ry="4"/><path d="M1 5h8M1.6 3h6.8M1.6 7h6.8"/></svg>
        </span>
        WWW.peltonmarsh.com
      </li>
    </ul>
  </section>

  <section class="card card--back" aria-label="Card back">
    <div class="brand">
      <span class="brand__mark"></span>
      <span class="brand__name">Pelton|Marsh &amp; Quillan</span>
    </div>
  </section>

</main>
</body>
</html>
```